Förderverein einer Kirchengemeinde sucht Flyer-Design
Zielgruppe
Wir sind ein Förderverein einer Kirchengemeinde, der sich für die kirchenmusikalische Arbeit einsetzt.
Wir wünschen uns ein niveauvolles und zeitgemäßes/modernes Flyerdesign, das die etablierten Konzertbesucher anspricht, aber vor allem auch Menschen erreicht und überzeugt, die (noch) nichts mit Kirche zu tun haben.
Das Alter der (Haupt-) Zielgruppe (Männer und Frauen) erstreckt sich von 45 bis 70 Jahren.
Aufgabenstellung
Bei der Wahl des Formates würden wir (aus der Sicht von Laien) ein zweimal gefaltetes DIN A4 quer Format nehmen. Aber wir lassen uns gerne überraschen und sind grundsätzlich für andere Lösungen offen.
Bitte den Abschnitt für Adress- und sonstige Dateneintragungen samt Kontodaten so gestalten und platzieren, dass man ihn leicht abtrennen und verschicken kann.
Der Flyer soll Kirchenmusik als lebendig und attraktiv darstellen und neue (jüngere) Mitglieder für den Freundeskreis werben.
Lassen Sie die Bilder sprechen!!

```html
<!DOCTYPE html>
<html lang="de">
<head>
<meta charset="utf-8">
<title>Freundeskreis Kantorei – Flyer</title>
<link href="https://fonts.googleapis.com/css2?family=Mulish:ital,wght@0,400;0,600;0,700;0,800;1,400&display=swap" rel="stylesheet">
<style>
:root{
  --red:#c0272d;
  --red-dark:#9e1b22;
  --red-light:#d23a3f;
  --paper:#ffffff;
  --ink:#555555;
  --ink-soft:#7a7a7a;
  --rule:#bdbdbd;
  --bar:#d6d6d6;
  --bg:#e6e6e6;
  --white:#ffffff;
}
*{box-sizing:border-box;margin:0;padding:0}
html,body{width:1200px;height:2268px;overflow:hidden;background:var(--bg);font-family:"Mulish",sans-serif;color:var(--ink)}
.canvas{position:relative;width:1200px;height:2268px}
.sheet{position:absolute;background:var(--paper);box-shadow:0 8px 24px rgba(0,0,0,.18);overflow:hidden}

/* Cover */
.cover{left:260px;top:90px;width:680px;height:475px}
.cover-photo{position:absolute;inset:0;background:linear-gradient(100deg,#b08a3c 0%,#8d8f92 18%,#c9c9c8 35%,#6f6a66 55%,#3a3532 70%,#c0a35a 100%)}
.cover-stripe{position:absolute;inset:0;background:#8a8a8a;clip-path:polygon(70% 0,73% 0,64% 100%,61% 100%);opacity:.6}
.cover-red{position:absolute;inset:0;background:linear-gradient(180deg,var(--red-dark),var(--red-light));clip-path:polygon(73% 0,100% 0,100% 100%,64% 100%)}
.cover-headline{position:absolute;left:92px;top:186px;color:var(--white);font-size:22px;font-weight:600;letter-spacing:.2px}
.cover-mark{position:absolute;right:24px;bottom:62px;width:180px;color:var(--white);font-size:18px;font-weight:700;line-height:1.25;letter-spacing:.5px}
.cover-mark .dot{display:block;width:54px;height:54px;border-radius:50%;background:var(--white);margin:0 0 150px 60px}

/* Back spread */
.back{left:150px;top:700px;width:900px;height:600px;display:flex}
.form-page{position:relative;width:460px;height:100%;padding:26px 26px 20px 30px;font-size:10.5px}
.form-title{color:var(--red);font-size:17px;font-weight:800;margin-bottom:10px}
.field{border-bottom:1px solid var(--rule);height:22px;padding-top:2px;color:var(--ink-soft)}
.field-row{display:flex;gap:14px}
.field-row .field{flex:1}
.bar{background:var(--bar);font-weight:700;font-size:11.5px;padding:3px 6px;margin:12px 0 6px;color:#444}
.checks{display:flex;gap:20px;margin-bottom:4px}
.checks ul{list-style:none;flex:1}
.checks li{margin-bottom:4px;display:flex;align-items:center;gap:5px}
.box{width:9px;height:9px;border:1px solid #777;flex:none}
.note{font-style:italic;font-size:9.5px}
.mandate{margin-top:8px;line-height:1.4}
.small{font-style:italic;font-size:9.5px;margin-top:6px}
.account{margin-top:12px;display:flex;gap:10px;line-height:1.45}
.account strong{color:#444;font-size:11.5px}
.cut-line{position:absolute;right:0;top:0;bottom:0;border-right:2px dashed #999}
.cut-label{position:absolute;right:6px;bottom:14px;font-size:8px;color:#999;writing-mode:vertical-rl;transform:rotate(180deg)}
.contact-page{width:440px;height:100%;display:flex;flex-direction:column}
.ensemble-photo{height:250px;background:linear-gradient(180deg,#b9b4aa 0%,#d8d4cc 40%,#ece9e4 60%,#6a6a6a 100%)}
.contact-panel{flex:1;background:linear-gradient(180deg,var(--red-dark),var(--red-light));color:var(--white);padding:20px 30px;font-size:13px;line-height:1.4}
.panel-mark{font-weight:700;font-size:13px;letter-spacing:.5px;margin-bottom:14px;display:flex;align-items:center;gap:8px}
.panel-mark .dot{width:14px;height:14px;border-radius:50%;background:var(--white)}
.contact-panel p{margin-bottom:10px}
.contact-panel .address{font-weight:800;font-size:14px}
.contact-panel .web{font-weight:800}

/* Inside spread */
.inside{left:50px;top:1470px;width:1100px;height:700px;display:flex}
.panel{position:relative;width:33.333%;height:100%;overflow:hidden}
.intro-photo{position:absolute;left:0;top:0;width:100%;height:300px;background:linear-gradient(135deg,#3b2a1e 0%,#c9b48a 35%,#e8dcc1 50%,#7a4a2e 75%,#2c1d14 100%);clip-path:polygon(0 0,100% 0,100% 55%,0 100%)}
.intro-text{position:absolute;left:28px;right:28px;top:260px;font-size:12px;line-height:1.5}
.intro-title{color:var(--red);font-size:20px;font-weight:800;line-height:1.15;margin-bottom:12px}
.intro-lead{margin-bottom:14px}
.intro-sub{color:var(--red);font-weight:800;font-size:13px;margin-bottom:6px}
.intro-text ul{list-style:none}
.intro-text li{margin-bottom:5px}
.organ-photo{position:absolute;inset:0;background:linear-gradient(180deg,#8a6a3a 0%,#b9a36e 20%,#d9d6d0 45%,#a8a39b 70%,#f0ece4 100%)}
.organ-caption{position:absolute;left:28px;top:30px;color:var(--white);font-size:16px;font-weight:700}
.reasons{background:linear-gradient(180deg,var(--red-dark),var(--red-light));color:var(--white);padding:34px 30px;font-size:13px;line-height:1.45}
.reasons p{margin-bottom:12px}
.reasons ul{list-style:none}
.reasons li{margin-bottom:12px}
</style>
</head>
<body>
<div class="canvas">

  <section class="sheet cover">
    <div class="cover-photo" role="img" aria-label="Nahaufnahme silberner Orgelpfeifen mit vergoldetem Schnitzwerk"></div>
    <div class="cover-stripe"></div>
    <div class="cover-red"></div>
    <h1 class="cover-headline">Kirchenmusik braucht Freunde…</h1>
    <div class="cover-mark"><span class="dot"></span>FREUNDESKREIS<br>KANTOREI</div>
  </section>

  <section class="sheet back">
    <div class="form-page">
      <h2 class="form-title">Beitrittserklärung</h2>
      <div class="field">Name, Vorname</div>
      <div class="field">für die Institution/Firma + persönlich</div>
      <div class="field">Straße, Hausnr., PLZ, Ort</div>
      <div class="field-row"><div class="field">Telefon/Handy</div><div class="field">Geburtstag</div></div>
      <div class="field-row"><div class="field">Emailadresse</div><div class="field">Datum, Unterschrift</div></div>

      <div class="bar">Mitgliedsbeiträge</div>
      <div class="checks">
        <ul>
          <li><span class="box"></span>Einzelpersonen € 20,-</li>
          <li><span class="box"></span>Ehepaare/Partnerschaften € 32,-</li>
          <li><span class="box"></span>Institutionen/Firmen € 95,-</li>
          <li class="note">(jeweils Mindestbeiträge)</li>
        </ul>
        <ul>
          <li><span class="box"></span>Frei wählbarer Betrag : €</li>
          <li><span class="box"></span>Ich benötige eine Spendenbescheinigung</li>
          <li><span class="box"></span>Einmalige Spende (ohne Mitgliedschaft)</li>
        </ul>
      </div>

      <div class="bar">SEPA-Lastschriftmandat</div>
      <div class="field-row"><div class="field">IBAN</div></div>
      <div class="field-row"><div class="field">Kreditinstitut</div><div class="field">BIC</div></div>
      <div class="field-row"><div class="field">Kontoinhaber</div></div>
      <p class="mandate">Hiermit ermächtige ich den Freundeskreis Kantorei den von mir zu entrichtenden Mitgliedsbeitrag von meinem Konto einzuziehen.</p>
      <div class="field">Ort, Datum, Unterschrift</div>
      <p class="small">Der Einzug der Mitgliedsbeiträge erfolgt zu Beginn eines Kalenderjahres</p>

      <div class="account">
        <strong>Spendenkonto:</strong>
        <div>Sparkasse Wendelstadt<br>IBAN: DE 00 1234 5678 9000 0000 00<br>BIC: SPKADE21XXX<br>Verwendungszweck bei Einzelspenden unter Angabe der Kostenstelle …</div>
      </div>
      <div class="cut-line"></div>
      <span class="cut-label">hier abtrennen</span>
    </div>

    <div class="contact-page">
      <div class="ensemble-photo" role="img" aria-label="Gruppenfoto des Posaunenchors mit Blechblasinstrumenten vor einem hellen Gebäude"></div>
      <div class="contact-panel">
        <div class="panel-mark">FREUNDESKREIS <span class="dot"></span> KANTOREI</div>
        <p>Wenn Sie die Kirchenmusik an St. Lamberti als Mitglied im <strong>Freundeskreis Kantorei</strong> fördern möchten, senden Sie die ausgefüllte Beitrittserklärung an den</p>
        <p class="address">Freundeskreis Kantorei,<br>Kirchengemeinde St. Lamberti,<br>Lindenweg 7, 31234 Wendelstadt,<br>Tel.: 01234-567890,<br>info@kantorei-lamberti.de</p>
        <p>Nähere Informationen finden Sie unter<br><span class="web">www.kirchenmusik-wendelstadt.de</span></p>
      </div>
    </div>
  </section>

  <section class="sheet inside">
    <div class="panel">
      <div class="intro-photo" role="img" aria-label="Hände auf den Tasten eines Orgelspieltischs mit Registerzügen"></div>
      <div class="intro-text">
        <h2 class="intro-title">Kirchenmusik<br>braucht Freunde</h2>
        <p class="intro-lead">Im Jahr 1999 gegründet, unterstützt der Freundeskreis Kantorei die vielfältigen musikalischen Aktivitäten an der St. Lamberti-Kirche. Wir laden Sie ein, Mitglied zu werden!</p>
        <h3 class="intro-sub">Mit Ihrem Beitrag …</h3>
        <ul>
          <li>… bereichern Sie Wendelstadts kulturelle Landschaft durch den Erhalt und Ausbau unseres hohen kirchenmusikalischen Niveaus</li>
          <li>… stärken Sie das Ehrenamt</li>
          <li>… ermöglichen Sie der Kantorei, dem Posaunenchor, dem Kinderchor und dem Flötenensemble regelmäßige Probenarbeit, Probenwochenenden und die Anschaffung von Notenmaterial</li>
          <li>… erhalten Sie die historische Johann Brandt Orgel von 1748</li>
          <li>… fördern Sie die Ausbildung kirchenmusikalischen Nachwuchses</li>
        </ul>
      </div>
    </div>

    <div class="panel">
      <div class="organ-photo" role="img" aria-label="Barocke Orgel mit goldverziertem Prospekt und silbernen Pfeifen"></div>
      <p class="organ-caption">Mitglieder haben gute Gründe:</p>
    </div>

    <div class="panel reasons">
      <p>Sie…</p>
      <ul>
        <li>… erhalten ermäßigte Eintrittspreise von gemeindeeigenen Konzerten</li>
        <li>… können Konzertkarten vor dem öffentlichen Verkauf erwerben</li>
        <li>… gestalten die Arbeit des Freundeskreises in den jährlichen Mitgliederversammlungen aktiv mit</li>
        <li>… erhalten aktuelle Informationen über Veranstaltungen der Gemeinde bequem per Email und profitieren so zu allererst</li>
        <li>… können den Mitgliedsbeitrag steuerlich absetzen und erhalten eine Spendenbescheinigung</li>
        <li>… können an Ausflügen des Freundeskreises teilnehmen</li>
      </ul>
    </div>
  </section>

</div>
</body>
</html>
```